Movie Poster - Beneath The Amber Tide

Documentary-film poster design.
Attached is a PDF brief with information on what is required and examples of poster designs I like.

The project is a true crime / mystery documentary film. Set in the Soviet Union in 1959.

Colors
3276b5
85abd2
ec1f27

```html
<!DOCTYPE html>
<html lang="en">
<head>
<meta charset="utf-8">
<title>Beneath The Amber Tide — Poster</title>
<link rel="stylesheet" href="https://fonts.googleapis.com/css2?family=Bebas+Neue&family=Montserrat:wght@300;400;600;700&family=Russo+One&display=swap">
<style>
  :root {
    --navy-deep: #0f2142;
    --navy: #1d3a66;
    --blue: #3276b5;
    --blue-soft: #85abd2;
    --mist: #e9eef3;
    --slate: #6f86a6;
    --red: #ec1f27;
    --white: #ffffff;
  }
  html, body {
    margin: 0;
    padding: 0;
    width: 900px;
    height: 1200px;
    overflow: hidden;
    background: var(--navy-deep);
  }
  .poster {
    position: relative;
    width: 900px;
    height: 1200px;
    overflow: hidden;
    color: var(--white);
    font-family: "Bebas Neue", "Arial Narrow", sans-serif;
  }
  .poster__scene {
    position: absolute;
    inset: 0;
    background:
      radial-gradient(ellipse 70% 18% at 50% 67%, rgba(255,255,255,0.95), rgba(255,255,255,0) 70%),
      radial-gradient(ellipse 30% 8% at 30% 88%, rgba(60,80,110,0.55), rgba(60,80,110,0) 70%),
      linear-gradient(180deg,
        var(--navy-deep) 0%,
        var(--navy) 16%,
        #3d5f88 34%,
        #8fa9c4 50%,
        var(--mist) 64%,
        #c9d3de 72%,
        #8799b3 84%,
        #4f6483 100%);
  }
  .headline {
    position: absolute;
    top: 30px;
    left: 0;
    right: 0;
    text-align: center;
    font-size: 46px;
    letter-spacing: 3px;
    line-height: 1;
    margin: 0;
    font-weight: 400;
  }
  .taglines {
    position: absolute;
    top: 132px;
    left: 0;
    right: 0;
    margin: 0;
    padding: 0;
    list-style: none;
    text-align: center;
    font-family: "Montserrat", sans-serif;
    font-weight: 300;
    font-variant: small-caps;
    font-size: 21px;
    letter-spacing: 1.5px;
    color: #e4ecf5;
  }
  .taglines li { height: 43px; }
  .title {
    position: absolute;
    top: 490px;
    left: 0;
    right: 0;
    margin: 0;
    text-align: center;
    color: var(--red);
    opacity: 0.9;
    font-weight: 400;
  }
  .title__lead {
    display: block;
    font-family: "Montserrat", sans-serif;
    font-weight: 700;
    font-size: 42px;
    letter-spacing: 2px;
    line-height: 1;
  }
  .title__main {
    display: block;
    font-family: "Russo One", sans-serif;
    font-size: 150px;
    letter-spacing: 6px;
    line-height: 1;
    margin-top: 8px;
  }
  .title__tail {
    display: block;
    font-family: "Montserrat", sans-serif;
    font-weight: 600;
    font-size: 54px;
    letter-spacing: 4px;
    line-height: 1;
    margin-top: 6px;
  }
  .credits {
    position: absolute;
    top: 928px;
    left: 0;
    right: 0;
    height: 60px;
  }
  .credit {
    position: absolute;
    width: 200px;
    text-align: center;
    transform: translateX(-50%);
  }
  .credit__role {
    display: block;
    font-family: "Montserrat", sans-serif;
    font-size: 14px;
    letter-spacing: 0.5px;
    line-height: 1;
  }
  .credit__name {
    display: block;
    font-size: 40px;
    line-height: 1;
    margin-top: 2px;
  }
  .credit--director { left: 238px; }
  .credit--screenplay { left: 473px; }
  .credit--story { left: 700px; }
  .billing {
    position: absolute;
    top: 1006px;
    left: 0;
    right: 0;
    text-align: center;
    line-height: 1;
  }
  .billing__row {
    margin: 0 0 10px;
    font-size: 22px;
    letter-spacing: 0.3px;
    white-space: nowrap;
  }
  .billing__small { font-size: 12px; }
  .billing__pair { margin: 0 7px; white-space: nowrap; }
  .billing__label {
    display: inline-block;
    font-size: 8px;
    line-height: 0.95;
    text-align: right;
    vertical-align: middle;
    margin-right: 3px;
  }
  .release {
    position: absolute;
    top: 1110px;
    left: 0;
    right: 0;
    text-align: center;
    font-size: 50px;
    line-height: 1;
    word-spacing: 22px;
  }
  .website {
    position: absolute;
    top: 1165px;
    left: 0;
    right: 0;
    text-align: center;
    font-size: 20px;
    letter-spacing: 0.5px;
  }
</style>
</head>
<body>
<main class="poster">
  <div class="poster__scene" role="img" aria-label="Photograph of a towering snow-covered mountain under a dark blue sky, with a line of hikers on skis walking through blowing snow in the foreground"></div>

  <h2 class="headline">The true story of the Dyatlov Pass incident</h2>

  <ul class="taglines">
    <li>Nine dead hikers</li>
    <li>Sixty years of secrets</li>
    <li>Russia’s greatest mystery uncovered</li>
  </ul>

  <h1 class="title">
    <span class="title__lead">BENEATH THE</span>
    <span class="title__main">AMBER</span>
    <span class="title__tail">TIDE</span>
  </h1>

  <section class="credits">
    <div class="credit credit--director"><span class="credit__role">DIRECTED BY</span><span class="credit__name">Director</span></div>
    <div class="credit credit--screenplay"><span class="credit__role">SCREENPLAY BY</span><span class="credit__name">Writer</span></div>
    <div class="credit credit--story"><span class="credit__role">STORY BY</span><span class="credit__name">Writer</span></div>
  </section>

  <section class="billing">
    <p class="billing__row">Northlight <span class="billing__small">PRESENTS A</span> Northlight <span class="billing__small">PRODUCTION IN ASSOCIATION WITH</span> Studio PB Actor Name Actor Name "Movie Title"</p>
    <p class="billing__row">
      <span class="billing__pair"><span class="billing__label">CASTING<br>BY</span>Casting Crew</span>
      <span class="billing__pair"><span class="billing__label">MUSIC<br>BY</span>Composer</span>
      <span class="billing__pair"><span class="billing__label">COSTUME<br>DESIGNER</span>Costume Designer</span>
      <span class="billing__pair"><span class="billing__label">EDITED<br>BY</span>Editor</span>
      <span class="billing__pair"><span class="billing__label">PRODUCTION<br>DESIGNER</span>Production Designer</span>
      <span class="billing__pair"><span class="billing__label">PRODUCED<br>BY</span>Producer</span>
    </p>
    <p class="billing__row">
      <span class="billing__pair"><span class="billing__label">DIRECTOR OF<br>PHOTOGRAPHY</span>Director of Photography</span>
      <span class="billing__pair"><span class="billing__label">CO-EXECUTIVE<br>PRODUCER</span>Co-Executive Producer</span>
      <span class="billing__pair"><span class="billing__label">EXECUTIVE<br>PRODUCER</span>Executive Producer</span>
    </p>
  </section>

  <p class="release" style="margin:0;">Coming Soon Month Year</p>
  <p class="website" style="margin:0;">www.ambertidefilm.com</p>
</main>
</body>
</html>
```